Hal's Remedies Business Card Design Project

I need a business card designed for my pharmacy Hal's Remedies. I would like just the logo on one side, maybe with black background and white lettering. The other side I would also like to include my logo which is attached. Also, please include my name and the following information:
Hal Norwick Owner/Pharm D.
Business address is 7163 N Birch Rd Sioux Falls, SD 57291.
Phone number is 605-318-6027 and fax # is 605-318-6031.
my email address is hal@halsremedies.example.
My website is www.halsremedies.example.
My business hours are Monday-Friday 8am-7 pm. Saturday 8am-12 pm. Sunday Closed.
I would like the design to include my logo colors, black, white, and neon green. Silver may be added as a highlight. Thanks.
Pharmacy
See above in product description

```html
<!DOCTYPE html>
<html lang="en">
<head>
<meta charset="utf-8">
<title>Hal's Remedies – Business Card</title>
<link href="https://fonts.googleapis.com/css2?family=Lato:wght@400;700;900&display=swap" rel="stylesheet">
<style>
  :root {
    --ink: #1a1a1a;
    --black: #0b0b0b;
    --white: #ffffff;
    --neon: #8cc63f;
    --silver: #cfcfcf;
    --faint: #ececec;
    --stage: #e9e9e6;
  }
  * { box-sizing: border-box; margin: 0; padding: 0; }
  html, body { width: 1200px; height: 900px; overflow: hidden; }
  body {
    background: var(--stage);
    font-family: 'Lato', Arial, sans-serif;
    color: var(--ink);
    position: relative;
  }
  .card {
    position: absolute;
    left: 250px;
    width: 700px;
    height: 400px;
    overflow: hidden;
    box-shadow: 0 6px 18px rgba(0,0,0,.18);
  }
  .card--front { top: 36px; background: var(--black); display: flex; flex-direction: column; align-items: center; justify-content: center; gap: 18px; }
  .card--back { top: 464px; background: var(--white); }

  .brand-mark { width: 26px; height: 26px; border-radius: 50%; background: var(--neon); }
  .front-name { color: var(--white); font-weight: 900; font-size: 50px; letter-spacing: -.5px; }

  .back-decor {
    position: absolute; right: -70px; top: -120px;
    width: 330px; height: 330px; border-radius: 50%;
    background: var(--faint);
  }
  .brand-row { position: absolute; left: 46px; top: 62px; display: flex; align-items: center; gap: 16px; }
  .brand-row .brand-mark { width: 20px; height: 20px; }
  .brand-divider { width: 2px; height: 42px; background: var(--ink); }
  .brand-name { font-weight: 900; font-size: 30px; }
  .address { position: absolute; left: 46px; top: 124px; font-weight: 700; font-size: 15px; }

  .rule { position: absolute; left: 46px; right: 40px; top: 168px; height: 2px; background: var(--neon); }

  .hours { position: absolute; right: 40px; top: 186px; text-align: right; font-weight: 700; font-size: 16px; line-height: 1.45; }

  .person { position: absolute; left: 46px; top: 212px; }
  .person-name { font-weight: 700; font-size: 26px; line-height: 1.05; }
  .person-title { font-weight: 700; font-size: 16px; }
  .person-rule { width: 200px; height: 2px; background: var(--neon); margin-top: 6px; }

  .contacts { position: absolute; left: 46px; top: 292px; list-style: none; font-weight: 700; font-size: 16px; }
  .contacts li { display: flex; align-items: center; gap: 14px; height: 24px; }
  .contacts svg { width: 17px; height: 17px; fill: var(--ink); flex: none; }
</style>
</head>
<body>
  <section class="card card--front">
    <div class="brand-mark"></div>
    <div class="front-name">Hal's Remedies</div>
  </section>

  <section class="card card--back">
    <div class="back-decor"></div>
    <div class="brand-row">
      <div class="brand-mark"></div>
      <div class="brand-divider"></div>
      <div class="brand-name">Hal's Remedies</div>
    </div>
    <div class="address">7163 N Birch Rd, Sioux Falls, SD 57291</div>
    <div class="rule"></div>
    <div class="hours">
      <div>Monday - Friday 8 am-7 pm</div>
      <div>Saturday 8 am-12 pm</div>
      <div>Sunday Closed</div>
    </div>
    <div class="person">
      <div class="person-name">Hal Norwick</div>
      <div class="person-title">Owner/Pharm D</div>
      <div class="person-rule"></div>
    </div>
    <ul class="contacts">
      <li><svg viewBox="0 0 24 24"><path d="M6.6 10.8a15 15 0 0 0 6.6 6.6l2.2-2.2c.3-.3.7-.4 1-.2 1.1.4 2.3.6 3.6.6.6 0 1 .4 1 1V20c0 .6-.4 1-1 1A17 17 0 0 1 3 4c0-.6.4-1 1-1h3.5c.6 0 1 .4 1 1 0 1.3.2 2.5.6 3.6.1.3 0 .7-.2 1z"/></svg>605-318-6027</li>
      <li><svg viewBox="0 0 24 24"><path d="M6 2h12v5H6zM3 8h18a1 1 0 0 1 1 1v8h-4v5H6v-5H2V9a1 1 0 0 1 1-1zm5 8v4h8v-4z"/></svg>605-318-6031</li>
      <li><svg viewBox="0 0 24 24"><path d="M2 5h20v14H2zm2 2v.5l8 5 8-5V7l-8 5z"/></svg>hal@halsremedies.example</li>
      <li><svg viewBox="0 0 24 24"><path d="M12 2a10 10 0 1 0 0 20 10 10 0 0 0 0-20zm0 2c.9 0 2.1 1.6 2.6 4H9.4C9.9 5.6 11.1 4 12 4zM4.3 10h4.8a17 17 0 0 0 0 4H4.3a8 8 0 0 1 0-4zm6.8 0h1.8v0h2a15 15 0 0 1 0 4h-3.8a15 15 0 0 1 0-4zm5.8 0h2.8a8 8 0 0 1 0 4h-2.8a17 17 0 0 0 0-4zM9.4 16h5.2c-.5 2.4-1.7 4-2.6 4s-2.1-1.6-2.6-4z"/></svg>www.halsremedies.example</li>
    </ul>
  </section>
</body>
</html>
```